Asia based real estate financing firm needs and AWESOME design for a biz card -Harborline Lending Partners

Looking for a stylish, & corporate-looking business card for a real estate financing brokerage firm in Asia, offering global mortgage loans. I uploaded our current logos. We would like to add a splash of color (perhaps the house icon) or any other suggestions are open. For the winning designer, we have a lot of work! Thanks and best of luck!

Target Market(s)

Real estate investors globally. We want to look more like a BANK and NOT a real estate company. Please don't play up on a "house" design.

Industry/Entity Type

Banking

Contact Information for Business Card

Harborline Lending Partners
Peter Walsh
Co-Founder | Partner

42 Kelvin Street, Suite 310
Singapore 074219
www.hlp-lend.example
peterwalsh@hlp-lend.example
+65 555-0147
WeChat: peterwalsh

Colors

Designer to choose colors to be used in the design.

Requirements
Must have
• Must have the standard business requirements for a card; name, address, email, etc
• Can be horizontal or vertical.
Nice to have
• It would be great to see some sort of variation to the logo with a pop of color. Red is good as we're in Asia, however, other options work as well.
• Our tag line is - Borderless mortgages. It doesn't have to be on the card but might be nice.
• I'd like to start seeing our tagline within the cards as well. - Borderless mortgages.
• Also, please add our location. The location for this card is Singapore so perhaps it can be highlighted or emphasised in some way.
• Singapore | Hong Kong | Shanghai | Manila
• As we will soon open an office in Shanghai, having an option for both languages would be great.
Should not have
• I'm exceited and open to your creativity ... knock it out of the park!

```html
<!DOCTYPE html>
<html lang="en">
<head>
<meta charset="utf-8">
<title>Harborline Lending Partners – Business Card</title>
<link rel="stylesheet" href="https://fonts.googleapis.com/css2?family=Roboto:wght@400;500;700&display=swap">
<style>
  :root {
    --brand-red: #c4161c;
    --ink: #1a1a1a;
    --text-grey: #555555;
    --rule-grey: #9a9a9a;
    --strip-grey: #b9b9b9;
    --paper: #ffffff;
    --backdrop: #e4e4e4;
  }
  * { box-sizing: border-box; margin: 0; padding: 0; }
  html, body {
    width: 1125px; height: 1200px; overflow: hidden;
    background: var(--backdrop);
    font-family: "Roboto", Arial, sans-serif;
  }
  .canvas { position: relative; width: 1125px; height: 1200px; }

  .card {
    position: absolute; left: 150px; width: 826px; height: 470px;
    overflow: hidden;
  }
  .card--front { top: 98px; background: var(--paper); }
  .card--back { top: 631px; background: var(--brand-red); }

  /* Front */
  .wordmark {
    position: absolute; right: 54px; top: 92px;
    text-align: right; color: var(--ink);
    font-weight: 500; font-size: 32px; line-height: 1.3;
    letter-spacing: 3px; text-transform: uppercase;
    white-space: nowrap;
  }
  .person { position: absolute; left: 44px; top: 230px; }
  .person__name {
    color: var(--brand-red); font-weight: 700; font-size: 30px;
    text-transform: uppercase; line-height: 1;
  }
  .person__title {
    margin-top: 6px; color: var(--text-grey); font-size: 20px;
  }
  .divider {
    position: absolute; left: 46px; right: 50px; top: 311px;
    height: 2px; background: var(--rule-grey);
  }
  .contacts { position: absolute; left: 44px; top: 332px; list-style: none; }
  .contacts li {
    display: flex; align-items: center; gap: 12px;
    height: 26px; color: var(--text-grey); font-size: 19px;
    white-space: nowrap;
  }
  .contacts svg { width: 18px; height: 18px; flex: none; }
  .address {
    position: absolute; right: 50px; top: 334px;
    text-align: right; color: var(--text-grey);
    font-size: 19px; line-height: 25px; font-style: normal;
    white-space: nowrap;
  }
  .bottom-strip {
    position: absolute; left: 0; bottom: 0; width: 480px; height: 7px;
    background: var(--strip-grey);
  }
  .web-band {
    position: absolute; right: 0; bottom: 0; width: 360px; height: 36px;
    background: var(--brand-red);
    clip-path: polygon(36px 0, 100% 0, 100% 100%, 0 100%);
    color: #fff; font-size: 16px; letter-spacing: 3px;
    display: flex; align-items: center; justify-content: flex-end;
    padding-right: 22px; text-transform: uppercase;
    white-space: nowrap;
  }

  /* Back */
  .back-field { position: absolute; inset: 0; background: var(--brand-red); }
  .wordmark--back {
    position: absolute; left: 0; right: 0; top: 190px;
    text-align: center; color: #fff;
    font-weight: 500; font-size: 36px; line-height: 1.3;
    letter-spacing: 4px; text-transform: uppercase;
    white-space: nowrap;
  }
</style>
</head>
<body>
<main class="canvas">

  <section class="card card--front" aria-label="Business card front">
    <div class="wordmark">Harborline<br>Lending Partners</div>

    <div class="person">
      <p class="person__name">Peter Walsh</p>
      <p class="person__title">Co-Founder | Partner</p>
    </div>

    <div class="divider"></div>

    <ul class="contacts">
      <li>
        <svg viewBox="0 0 24 24" aria-hidden="true"><path fill="#c4161c" d="M6.6 10.8a15.2 15.2 0 0 0 6.6 6.6l2.2-2.2a1 1 0 0 1 1-.25 11.4 11.4 0 0 0 3.6.57 1 1 0 0 1 1 1V20a1 1 0 0 1-1 1A17 17 0 0 1 3 4a1 1 0 0 1 1-1h3.5a1 1 0 0 1 1 1c0 1.25.2 2.45.57 3.57a1 1 0 0 1-.25 1z"/></svg>
        +65 555-0147
      </li>
      <li>
        <svg viewBox="0 0 24 24" aria-hidden="true"><rect x="2" y="5" width="20" height="14" fill="#c4161c"/><path d="M2 5l10 8 10-8" fill="none" stroke="#fff" stroke-width="1.8"/></svg>
        peterwalsh@hlp-lend.example
      </li>
      <li>
        <svg viewBox="0 0 24 24" aria-hidden="true"><rect x="2" y="2" width="20" height="20" rx="3" fill="#c4161c"/></svg>
        peterwalsh
      </li>
    </ul>

    <address class="address">
      42 Kelvin Street<br>
      Suite 310<br>
      Singapore 074219
    </address>

    <div class="bottom-strip"></div>
    <div class="web-band">www.hlp-lend.example</div>
  </section>

  <section class="card card--back" aria-label="Business card back">
    <div class="back-field" role="img" aria-label="Red background with a repeating faint brand pattern"></div>
    <div class="wordmark--back">Harborline<br>Lending Partners</div>
  </section>

</main>
</body>
</html>
```